New AI Company Needs a Powerpoint

We are a new type of AI company called KestrelMind. Our AI uses human inspired approaches and put the human on the center of all our solutions. We need a standard company powerpoint design to use with potential investors, customers and partners to introduce our company and explain how the approach we take to AI is very different than others.
We want a design that is clean, modern, and playful. We do not want it to look overly robotic or cliche techy. Our mission is to remind the world that technology is a tool to be used to enhance and assist not to replace real humans.
We want a design that can show boring things (like financial info) in engaging ways.

Please use colors in logo variations along with a vibrant complementary color palette of your choosing,

Industry/Entity Type

Technology

Font styles to use
Sans Serif
Other font styles liked:
• Opensans

Colors
0054AA
0677BA
7BADD7
CADEEF
E8F1F8
0094D4
00A9DD
6FCCEA
C7EBF8
E9F6FB
00AB8E
00BBA5
67D7C9
C6EFE9
E9F9F6
59FF00
82FF00
B8FF75
E3FFCB
F4FFEA

Requirements
Must have
• Must incorporate logo colors and style

```html
<!DOCTYPE html>
<html lang="en">
<head>
<meta charset="utf-8">
<title>KestrelMind Presentation Template</title>
<link href="https://fonts.googleapis.com/css2?family=Ubuntu:wght@300;400;500;700&display=swap" rel="stylesheet">
<style>
:root{
  --navy:#1b2454;
  --navy-2:#1d3a86;
  --blue:#0054AA;
  --blue-2:#0677BA;
  --cyan:#0094D4;
  --cyan-2:#00A9DD;
  --teal:#00AB8E;
  --teal-2:#00BBA5;
  --ink:#2b3550;
  --grey:#6b7383;
  --line:#d6dbe4;
  --page:#c9cacd;
}
*{box-sizing:border-box;margin:0;padding:0}
html,body{width:1200px;height:2322px;overflow:hidden}
body{background:var(--page);font-family:"Ubuntu",sans-serif;color:var(--ink);position:relative}
.hero-band{position:absolute;left:0;top:0;width:1200px;height:720px;background:linear-gradient(180deg,#d5d8de,#c3c6cc)}
.brand{font-family:"Ubuntu",sans-serif;font-weight:700;letter-spacing:.08em;display:flex;align-items:center;gap:.35em;white-space:nowrap}
.brand .dot{display:inline-block;width:.9em;height:.9em;border-radius:50%;background:var(--cyan-2)}
.brand-top{position:absolute;left:950px;top:82px;font-size:24px;color:var(--navy)}
.hero-slide{position:absolute;left:230px;top:150px;width:740px;height:416px;overflow:hidden;box-shadow:0 12px 40px rgba(20,30,60,.35)}

.slide{position:absolute;width:374px;height:210px;overflow:hidden;background:#fff;font-family:"Ubuntu",sans-serif}
.dark{background:linear-gradient(125deg,#1a2252 0%,#1d3a86 55%,#19367c 100%);color:#fff}
.photo{position:absolute;background:linear-gradient(135deg,#5f7fb0,#1e3c80)}
.photo.light{background:linear-gradient(135deg,#dfe8f0,#9fb6cc)}
.photo.teal{background:linear-gradient(135deg,#7fb3c4,#2e6d8a)}
.photo.person{background:linear-gradient(180deg,#d9dde3,#8d95a3)}
.headart{position:absolute;background:radial-gradient(ellipse at 60% 55%,rgba(60,140,220,.55),rgba(30,70,150,0) 70%)}

.s-brand{position:absolute;font-size:8px;color:#fff}
.s-brand.dk{color:var(--navy)}
.title{position:absolute;font-weight:700;font-size:15px;line-height:1.2;text-transform:none}
.title .up{text-transform:uppercase}
.desc{position:absolute;font-size:4.6px;line-height:1.5;color:rgba(255,255,255,.85)}
.pill{position:absolute;background:var(--cyan-2);color:#fff;font-size:4.2px;text-align:center;line-height:8px;border-radius:1px}
.strip{position:absolute;left:0;bottom:0;width:100%;height:10px;background:#fff;color:var(--grey);font-size:2.8px;text-align:center;line-height:10px}

.foot-brand{position:absolute;left:9px;bottom:7px;font-size:4.2px;color:var(--navy)}
.foot-copy{position:absolute;right:12px;bottom:8px;font-size:2.6px;color:var(--grey)}
.foot-copy b{color:var(--cyan);font-weight:400;margin-left:4px}

.h{position:absolute;font-size:12px;font-weight:400;color:var(--ink)}
.h.center{left:0;width:100%;text-align:center}
.h.white{color:#fff}
.rule{position:absolute;height:1.5px;background:var(--cyan-2)}
.small{position:absolute;font-size:3.3px;line-height:1.45;color:var(--grey)}
.sub{position:absolute;font-size:5px;font-weight:500;color:var(--ink)}
.sub.cy{color:var(--cyan-2)}
.tiny-head{font-size:4.2px;font-weight:500;color:var(--cyan-2);display:block;margin-bottom:1px}

.toc{position:absolute;left:198px;top:32px;width:150px;color:#fff}
.toc h3{font-weight:400;font-size:12px;margin-bottom:8px}
.toc li{list-style:none;font-size:9.5px;font-weight:300;border-bottom:.6px solid rgba(255,255,255,.3);padding:3px 0;display:flex;gap:11px}

.cardbox{position:absolute;left:190px;width:156px;height:38px;border-radius:4px;color:#fff;display:flex;align-items:center}
.cardbox .ic{width:36px;height:100%;display:flex;align-items:center;justify-content:center;font-size:14px;border-right:.6px solid rgba(255,255,255,.5)}
.cardbox p{font-size:3.3px;line-height:1.4;padding:0 6px}
.bg-cyan{background:var(--cyan-2)}
.bg-blue{background:var(--blue)}
.bg-teal{background:var(--teal-2)}
.bg-navy{background:var(--navy)}

.team{position:absolute;top:50px;width:70px;text-align:center}
.team .pic{width:48px;height:66px;margin:0 auto 10px;position:relative;border:1.5px solid #fff}
.team b{display:block;font-size:5.5px;font-weight:500;color:var(--ink)}
.team i{display:block;font-style:normal;font-size:3.4px;color:var(--cyan-2);margin:1px 0 3px}
.team p{font-size:3.2px;line-height:1.4;color:var(--grey)}

.tl{position:absolute;top:70px;width:56px;text-align:center}
.tl .n{width:14px;height:14px;border-radius:50%;color:#fff;font-size:7px;line-height:14px;margin:0 auto 6px}
.tl b{display:block;font-size:4.2px;font-weight:400;color:var(--cyan-2);line-height:1.2;margin-bottom:3px}
.tl p{font-size:3.2px;line-height:1.4;color:var(--grey)}

.grid-item{position:absolute;width:150px;display:flex;gap:8px}
.grid-item .sq{width:14px;height:14px;flex:none;display:flex;align-items:center;justify-content:center}
.grid-item p{font-size:3.2px;line-height:1.4;color:var(--grey)}

.tcard{position:absolute;top:50px;width:88px;height:125px}
.tcard .pic{position:absolute;left:0;top:0;width:100%;height:66px}
.tcard .body{position:absolute;left:0;top:66px;width:100%;height:59px;color:#fff;text-align:center;padding:14px 5px 0}
.tcard .circ{position:absolute;left:35px;top:53px;width:18px;height:18px;border-radius:50%;border:1.3px solid #fff;display:flex;align-items:center;justify-content:center}
.tcard b{display:block;font-size:4.4px;font-weight:500;margin-bottom:3px}
.tcard p{font-size:3.2px;line-height:1.4}

.num{position:absolute;left:190px;width:156px;height:38px;border-radius:4px;color:#fff;display:flex;align-items:center}
.num span{width:36px;text-align:center;font-size:18px;font-weight:300;border-right:.6px solid rgba(255,255,255,.5)}
.num p{font-size:3.2px;line-height:1.4;padding:0 6px}

.ring-note{position:absolute;width:44px;font-size:2.8px;line-height:1.35;color:var(--grey);text-align:center}
.donut-cap{position:absolute;top:142px;width:80px;text-align:center}
.donut-cap b{display:block;font-size:5px;font-weight:400;color:var(--cyan-2);margin-bottom:2px}
.donut-cap p{font-size:3.2px;line-height:1.4;color:var(--grey)}
.contact{position:absolute;left:26px;top:108px;color:#fff}
.contact h4{font-size:6px;font-weight:400;color:var(--cyan-2);margin-bottom:3px}
.contact p{font-size:4px;margin-bottom:6px}
.contact li{list-style:none;font-size:4.2px;margin-bottom:4px;display:flex;gap:5px;align-items:center}
.contact li i{width:5px;height:5px;border:.6px solid var(--cyan-2);border-radius:1px;display:inline-block}
</style>
</head>
<body>

<section class="hero-band" aria-label="Cover slide preview">
  <div class="brand brand-top"><span>KESTRELMIND</span><span class="dot"></span></div>

  <article class="slide dark hero-slide">
    <div class="headart" role="img" aria-label="Glowing blue digital head outline over a data grid" style="left:320px;top:20px;width:420px;height:370px"></div>
    <div class="s-brand brand" style="left:62px;top:60px;font-size:16px">KESTRELMIND <span class="dot"></span></div>
    <div class="title" style="left:62px;top:140px;font-size:32px"><span class="up">Presentation Title</span><br>Goes Here!</div>
    <div style="position:absolute;left:62px;top:232px;width:70px;height:3px;background:var(--cyan-2)"></div>
    <div class="desc" style="left:62px;top:252px;font-size:10.5px">Lorem ipsum dolor sit amet, consectetur adipiscing elit.<br>dui ex. Curabitur dapibus dignissim dui, in molestie metus feugiat sed.</div>
    <div class="pill" style="left:62px;top:310px;width:124px;height:20px;line-height:20px;font-size:9px">December 14, 2022</div>
    <div class="strip" style="height:24px;line-height:24px;font-size:6.5px">KestrelMind © 2022 All Rights Reserved.</div>
  </article>
</section>

<!-- Row 1 : cover variations -->
<article class="slide dark" style="left:26px;top:741px">
  <div class="headart" role="img" aria-label="Digital head outline over a data grid" style="left:170px;top:10px;width:210px;height:190px"></div>
  <div class="s-brand brand" style="left:27px;top:38px">KESTRELMIND <span class="dot"></span></div>
  <div class="title" style="left:27px;top:77px"><span class="up">Presentation Title</span><br>Goes Here!</div>
  <div class="desc" style="left:27px;top:126px">Lorem ipsum dolor sit amet, consectetur adipiscing elit.<br>dui ex. Curabitur dapibus dignissim dui, in molestie metus feugiat sed.</div>
  <div class="pill" style="left:27px;top:158px;width:74px">December 14, 2022</div>
  <div class="strip">KestrelMind © 2022 All Rights Reserved.</div>
</article>

<article class="slide dark" style="left:413px;top:741px">
  <div class="headart" role="img" aria-label="Digital head outline over a data grid" style="left:170px;top:10px;width:210px;height:190px"></div>
  <div class="s-brand brand" style="left:27px;top:38px">KESTRELMIND <span class="dot"></span></div>
  <div class="title" style="left:27px;top:77px"><span class="up">Presentation Title</span><br>Goes Here!</div>
  <div class="desc" style="left:27px;top:126px">Lorem ipsum dolor sit amet, consectetur adipiscing elit.<br>dui ex. Curabitur dapibus dignissim dui, in molestie metus feugiat sed.</div>
  <div class="pill" style="left:27px;top:158px;width:74px">December 14, 2022</div>
  <div class="strip">KestrelMind © 2022 All Rights Reserved.</div>
</article>

<article class="slide" style="left:800px;top:741px">
  <div class="photo" role="img" aria-label="Blue abstract technology light" style="left:187px;top:0;width:187px;height:180px;background:linear-gradient(135deg,#2a5fb5,#0f2a66)"></div>
  <div class="s-brand brand dk" style="left:27px;top:30px">KESTRELMIND <span class="dot"></span></div>
  <div style="position:absolute;left:0;top:64px;width:374px;height:116px;background:linear-gradient(90deg,#1c2556,#1d3a86);opacity:.93"></div>
  <div class="title" style="left:27px;top:80px;color:#fff"><span class="up">Presentation Title</span><br>Goes Here!</div>
  <div class="desc" style="left:27px;top:129px">Lorem ipsum dolor sit amet, consectetur adipiscing elit.<br>dui ex. Curabitur dapibus dignissim dui, in molestie metus feugiat sed.</div>
  <div class="pill" style="left:27px;top:166px;width:74px">December 14, 2022</div>
  <div class="strip" style="height:18px;line-height:18px">KestrelMind © 2022 All Rights Reserved.</div>
</article>

<!-- Row 2 -->
<article class="slide" style="left:26px;top:964px">
  <svg width="374" height="210" style="position:absolute;left:0;top:0">
    <polygon points="170,0 374,0 374,170 310,170" fill="#1d3a86"/>
    <polygon points="232,0 285,0 330,170 283,170" fill="#1f6fc8" opacity=".75"/>
  </svg>
  <div class="s-brand brand dk" style="left:27px;top:30px">KESTRELMIND <span class="dot"></span></div>
  <svg width="374" height="110" style="position:absolute;left:0;top:64px"><polygon points="0,0 200,0 232,110 0,110" fill="#1c2556"/><polygon points="200,0 374,0 374,110 232,110" fill="#1d3a86" opacity=".6"/></svg>
  <div class="title" style="left:27px;top:80px;color:#fff"><span class="up">Presentation Title</span><br>Goes Here!</div>
  <div class="desc" style="left:27px;top:129px">Lorem ipsum dolor sit amet, consectetur adipiscing elit.<br>dui ex. Curabitur dapibus dignissim dui, in molestie metus feugiat sed.</div>
  <div class="pill" style="left:27px;top:166px;width:74px">December 14, 2022</div>
  <div class="strip" style="height:18px;line-height:18px">KestrelMind © 2022 All Rights Reserved.</div>
</article>

<article class="slide dark" style="left:413px;top:964px">
  <div class="headart" role="img" aria-label="Line drawing of a digital human head" style="left:10px;top:30px;width:185px;height:160px"></div>
  <nav class="toc">
    <h3>Table of Contents</h3>
    <ul>
      <li><span>01</span>Title Goes Here</li>
      <li><span>02</span>Title Goes Here</li>
      <li><span>03</span>Title Goes Here</li>
      <li><span>04</span>Title Goes Here</li>
      <li><span>05</span>Title Goes Here</li>
    </ul>
  </nav>
</article>

<article class="slide" style="left:800px;top:964px">
  <div class="h" style="left:33px;top:30px">About Us</div>
  <div class="small" style="left:33px;top:60px;width:180px">Nunc placerat, arcu nec mattis fermentum, nisl mauris convallis nunc, ut luctus nunc nisl id ex. Nam semper tristique mauris, et vestibulum leo fringilla vel. Nulla id augue eleifend.</div>
  <div style="position:absolute;left:0;top:96px;width:374px;height:74px;background:var(--navy)"></div>
  <div class="small" style="left:33px;top:110px;width:124px;color:#fff">Phasellus eget commodo arcu. Nunc vitae semper dui. Integer venenatis, tellus sit amet interdum pretium, erat neque rhoncus turpis, a aliquam augue ligula eget erat. Nunc placerat, arcu nec mattis fermentum, nisl mauris convallis nunc.</div>
  <div class="small" style="left:160px;top:110px;width:124px;color:#fff">Phasellus eget commodo arcu. Nunc vitae semper dui. Integer venenatis, tellus sit amet interdum pretium, erat neque rhoncus turpis, a aliquam augue ligula eget erat. Nunc placerat, arcu nec mattis fermentum, nisl mauris convallis nunc.</div>
  <div class="photo" role="img" aria-label="Human hand reaching toward a robotic hand" style="left:234px;top:0;width:140px;height:210px;background:linear-gradient(135deg,#3c5870,#1a2a3d)"></div>
  <div class="foot-brand brand">KESTRELMIND</div>
  <div class="foot-copy">KestrelMind © 2022 All Rights Reserved.<b>6</b></div>
</article>

<!-- Row 3 -->
<article class="slide" style="left:26px;top:1187px">
  <div class="dark" style="position:absolute;left:0;top:0;width:374px;height:70px"></div>
  <div class="h center white" style="top:16px">Heading Goes Here</div>
  <div class="photo light" role="img" aria-label="Man using a holographic interface" style="left:22px;top:48px;width:162px;height:46px"></div>
  <div class="photo teal" role="img" aria-label="Close-up of an eye with a digital overlay" style="left:190px;top:48px;width:162px;height:46px"></div>
  <div class="sub" style="left:22px;top:104px">Heading Goes Here</div>
  <div class="small" style="left:22px;top:113px;width:160px">Phasellus eget commodo arcu. Nunc vitae semper dui. Integer venenatis, tellus sit amet interdum pretium, erat neque rhoncus turpis, a aliquam augue ligula eget erat.<br>• Phasellus eget commodo arcu. Nunc vitae semper dui.<br>• Integer venenatis, tellus sit amet interdum pretium.<br>• Nunc placerat, arcu nec mattis fermentum.<br>• Nam semper tristique mauris, et vestibulum leo.</div>
  <div class="sub" style="left:192px;top:104px">Heading Goes Here</div>
  <div class="small" style="left:192px;top:113px;width:160px">Phasellus eget commodo arcu. Nunc vitae semper dui. Integer venenatis, tellus sit amet interdum pretium, erat neque rhoncus turpis, a aliquam augue ligula eget erat.<br>• Phasellus eget commodo arcu. Nunc vitae semper dui.<br>• Integer venenatis, tellus sit amet interdum pretium.<br>• Nunc placerat, arcu nec mattis fermentum.<br>• Nam semper tristique mauris, et vestibulum leo.</div>
  <div class="foot-brand brand">KESTRELMIND</div>
  <div class="foot-copy">KestrelMind © 2022 All Rights Reserved.<b>7</b></div>
</article>

<article class="slide" style="left:413px;top:1187px">
  <div class="dark" style="position:absolute;left:240px;top:0;width:134px;height:170px"></div>
  <div class="h" style="left:33px;top:30px">Heading Goes Here</div>
  <div class="small" style="left:33px;top:52px;width:135px">Nunc placerat, arcu nec mattis fermentum, nisl mauris convallis nunc, ut luctus nunc nisl id ex. Nam semper tristique mauris, et vestibulum leo fringilla vel.<br><br>• Phasellus eget commodo arcu. Nunc vitae semper dui. Integer venenatis, tellus sit amet interdum pretium.<br>• Nunc placerat, arcu nec mattis fermentum, nisl mauris convallis nunc, ut luctus nunc nisl id ex.<br>• Nam semper tristique mauris, et vestibulum leo fringilla vel. Nulla id augue eleifend.<br>• Consequat massa. Pellentesque habitant morbi tristique senectus et netus.<br>• Phasellus eget commodo arcu. Nunc vitae semper dui.</div>
  <div class="cardbox bg-cyan" style="top:30px"><div class="ic"><svg width="13" height="11"><rect x=".5" y="2.5" width="12" height="8" rx="1" fill="none" stroke="#fff"/><rect x="4.5" y=".5" width="4" height="2" fill="none" stroke="#fff"/></svg></div><p>Phasellus eget commodo arcu. Nunc vitae semper dui. Integer venenatis, tellus sit amet interdum pretium, erat neque rhoncus turpis, a aliquam augue ligula eget erat.</p></div>
  <div class="cardbox bg-blue" style="top:74px"><div class="ic"><svg width="13" height="13"><circle cx="5" cy="5" r="4" fill="none" stroke="#fff" stroke-width="1.4"/><line x1="8" y1="8" x2="12" y2="12" stroke="#fff" stroke-width="1.6"/></svg></div><p>Phasellus eget commodo arcu. Nunc vitae semper dui. Integer venenatis, tellus sit amet interdum pretium, erat neque rhoncus turpis, a aliquam augue ligula eget erat.</p></div>
  <div class="cardbox bg-teal" style="top:118px"><div class="ic"><svg width="14" height="11"><rect x="1.5" y=".5" width="11" height="7.5" fill="none" stroke="#fff"/><line x1="0" y1="10" x2="14" y2="10" stroke="#fff"/></svg></div><p>Phasellus eget commodo arcu. Nunc vitae semper dui. Integer venenatis, tellus sit amet interdum pretium, erat neque rhoncus turpis, a aliquam augue ligula eget erat.</p></div>
  <div class="foot-brand brand">KESTRELMIND</div>
  <div class="foot-copy">KestrelMind © 2022 All Rights Reserved.<b>8</b></div>
</article>

<article class="slide" style="left:800px;top:1187px">
  <div class="h" style="left:33px;top:30px;line-height:1.25">Heading<br>Goes Here!</div>
  <div class="small" style="left:33px;top:68px;width:110px">Phasellus eget commodo arcu. Nunc vitae semper dui. Integer venenatis, tellus sit amet interdum pretium, erat neque rhoncus turpis, a aliquam augue ligula eget erat.<br><br>Nunc placerat, arcu nec mattis fermentum, nisl mauris convallis nunc, ut luctus nunc nisl id ex. Nam semper tristique mauris.<br><br>Nulla id augue eleifend, egestas ligula et, consequat massa. Pellentesque habitant morbi tristique senectus.</div>
  <div class="photo" role="img" aria-label="Human hand shaking a robotic hand" style="left:138px;top:31px;width:76px;height:120px;background:linear-gradient(135deg,#3a5568,#1b2b3b)"></div>
  <div class="photo light" role="img" aria-label="Man holding a tablet" style="left:218px;top:31px;width:76px;height:120px"></div>
  <div class="photo" role="img" aria-label="Hand touching a glowing digital screen" style="left:298px;top:31px;width:76px;height:120px;background:linear-gradient(135deg,#2d4fa6,#111d52)"></div>
  <div class="small" style="left:141px;top:156px;width:70px"><span class="sub" style="position:static;font-size:4.2px;display:block">Title Goes Here</span>Nam semper tristique mauris, et vestibulum leo fringilla vel.</div>
  <div class="small" style="left:221px;top:156px;width:70px"><span class="sub" style="position:static;font-size:4.2px;display:block">Title Goes Here</span>Nam semper tristique mauris, et vestibulum leo fringilla vel.</div>
  <div class="small" style="left:301px;top:156px;width:70px"><span class="sub" style="position:static;font-size:4.2px;display:block">Title Goes Here</span>Nam semper tristique mauris, et vestibulum leo fringilla vel.</div>
  <div class="foot-brand brand">KESTRELMIND</div>
  <div class="foot-copy">KestrelMind © 2022 All Rights Reserved.<b>9</b></div>
</article>

<!-- Row 4 -->
<article class="slide" style="left:26px;top:1410px">
  <div class="dark" style="position:absolute;left:0;top:0;width:374px;height:95px"></div>
  <div class="h center white" style="top:16px">Meet Our Team</div>
  <div class="team" style="left:32px"><div class="pic photo person" role="img" aria-label="Team member portrait"></div><b>Person Name</b><i>Job Title Goes Here</i><p>Lorem ipsum dolor sit amet, consectetur adipiscing elit. Vivamus eu dui ex. Curabitur dapibus dignissim dui.</p></div>
  <div class="team" style="left:113px"><div class="pic photo person" role="img" aria-label="Team member portrait"></div><b>Person Name</b><i>Job Title Goes Here</i><p>Lorem ipsum dolor sit amet, consectetur adipiscing elit. Vivamus eu dui ex. Curabitur dapibus dignissim dui.</p></div>
  <div class="team" style="left:194px"><div class="pic photo person" role="img" aria-label="Team member portrait"></div><b>Person Name</b><i>Job Title Goes Here</i><p>Lorem ipsum dolor sit amet, consectetur adipiscing elit. Vivamus eu dui ex. Curabitur dapibus dignissim dui.</p></div>
  <div class="team" style="left:275px"><div class="pic photo person" role="img" aria-label="Team member portrait"></div><b>Person Name</b><i>Job Title Goes Here</i><p>Lorem ipsum dolor sit amet, consectetur adipiscing elit. Vivamus eu dui ex. Curabitur dapibus dignissim dui.</p></div>
  <div class="foot-brand brand">KESTRELMIND</div>
  <div class="foot-copy">KestrelMind © 2022 All Rights Reserved.<b>10</b></div>
</article>

<article class="slide dark" style="left:413px;top:1410px">
  <div class="headart" role="img" aria-label="Line drawing of a digital human head" style="left:190px;top:20px;width:184px;height:170px"></div>
  <div class="title" style="left:27px;top:70px"><span class="up">Section Break</span><br>Title Goes Here</div>
  <div class="desc" style="left:27px;top:120px">Lorem ipsum dolor sit amet, consectetur adipiscing elit.<br>dui ex. Curabitur dapibus dignissim dui, in molestie metus feugiat sed.</div>
</article>

<article class="slide" style="left:800px;top:1410px">
  <div class="h center" style="top:16px">Heading Goes Here</div>
  <div class="rule" style="left:172px;top:36px;width:30px"></div>
  <div style="position:absolute;left:20px;top:77px;width:334px;border-top:.6px dashed var(--line)"></div>
  <div class="tl" style="left:32px"><div class="n bg-cyan">1</div><b>Heading<br>Goes Here</b><p>Phasellus eget commodo arcu. Nunc vitae semper dui. Integer venenatis, tellus sit amet interdum pretium.</p></div>
  <div class="tl" style="left:96px"><div class="n bg-blue">2</div><b>Heading<br>Goes Here</b><p>Phasellus eget commodo arcu. Nunc vitae semper dui. Integer venenatis, tellus sit amet interdum pretium.</p></div>
  <div class="tl" style="left:160px"><div class="n bg-teal">3</div><b>Heading<br>Goes Here</b><p>Phasellus eget commodo arcu. Nunc vitae semper dui. Integer venenatis, tellus sit amet interdum pretium.</p></div>
  <div class="tl" style="left:224px"><div class="n bg-cyan">4</div><b>Heading<br>Goes Here</b><p>Phasellus eget commodo arcu. Nunc vitae semper dui. Integer venenatis, tellus sit amet interdum pretium.</p></div>
  <div class="tl" style="left:288px"><div class="n bg-blue">5</div><b>Heading<br>Goes Here</b><p>Phasellus eget commodo arcu. Nunc vitae semper dui. Integer venenatis, tellus sit amet interdum pretium.</p></div>
  <div class="foot-brand brand">KESTRELMIND</div>
  <div class="foot-copy">KestrelMind © 2022 All Rights Reserved.<b>12</b></div>
</article>

<!-- Row 5 -->
<article class="slide" style="left:26px;top:1633px">
  <svg width="374" height="210" style="position:absolute;left:0;top:0">
    <path d="M138,22 A88,88 0 0 1 138,198" fill="none" stroke="#c9ced8" stroke-width="1.4"/>
    <g stroke="#1b2454" stroke-width=".8">
      <line x1="186" y1="26" x2="212" y2="26"/><line x1="219" y1="62" x2="240" y2="62"/><line x1="226" y1="98" x2="250" y2="98"/><line x1="219" y1="134" x2="240" y2="134"/><line x1="186" y1="170" x2="212" y2="170"/>
    </g>
    <circle cx="138" cy="22" r="3.5" fill="#9aa1ad"/>
    <circle cx="186" cy="26" r="3.5" fill="#1b2454"/>
    <circle cx="215" cy="62" r="3.5" fill="#00A9DD"/>
    <circle cx="226" cy="98" r="3.5" fill="#1b2454"/>
    <circle cx="215" cy="134" r="3.5" fill="#00A9DD"/>
    <circle cx="186" cy="170" r="3.5" fill="#1b2454"/>
    <circle cx="138" cy="198" r="3.5" fill="#9aa1ad"/>
  </svg>
  <div class="h" style="left:33px;top:36px">Heading Goes Here</div>
  <div class="small" style="left:33px;top:62px;width:135px;color:var(--cyan-2);font-size:3.8px">Nunc placerat, arcu nec mattis fermentum, nisl mauris convallis nunc, ut luctus nunc nisl id ex. Nam semper tristique mauris, et vestibulum leo fringilla vel.</div>
  <div class="small" style="left:33px;top:96px;width:135px">Phasellus eget commodo arcu. Nunc vitae semper dui. Integer venenatis, tellus sit amet interdum pretium, erat neque rhoncus turpis, a aliquam augue ligula eget erat. Nunc placerat, arcu nec mattis fermentum.<br><br>Augue eleifend, egestas ligula et, consequat massa. Pellentesque habitant morbi tristique senectus et netus et malesuada fames ac turpis egestas.</div>
  <div class="small" style="left:216px;top:18px;width:90px"><span class="tiny-head" style="color:var(--ink)">Title Goes Here</span>Phasellus eget commodo arcu. Nunc vitae semper dui.</div>
  <div class="small" style="left:246px;top:54px;width:90px"><span class="tiny-head">Title Goes Here</span>Phasellus eget commodo arcu. Nunc vitae semper dui.</div>
  <div class="small" style="left:254px;top:90px;width:90px"><span class="tiny-head" style="color:var(--ink)">Title Goes Here</span>Phasellus eget commodo arcu. Nunc vitae semper dui.</div>
  <div class="small" style="left:246px;top:126px;width:90px"><span class="tiny-head">Title Goes Here</span>Phasellus eget commodo arcu. Nunc vitae semper dui.</div>
  <div class="small" style="left:216px;top:162px;width:90px"><span class="tiny-head" style="color:var(--ink)">Title Goes Here</span>Phasellus eget commodo arcu. Nunc vitae semper dui.</div>
  <div class="foot-brand brand">KESTRELMIND</div>
  <div class="foot-copy">KestrelMind © 2022 All Rights Reserved.<b>13</b></div>
</article>

<article class="slide" style="left:413px;top:1633px">
  <div class="h center" style="top:16px">Heading Goes Here</div>
  <div class="rule" style="left:172px;top:36px;width:30px"></div>
  <div class="grid-item" style="left:33px;top:60px"><div class="sq bg-cyan"></div><p><span class="tiny-head">Title Goes Here</span>Phasellus eget commodo arcu. Nunc vitae semper dui. Integer venenatis, tellus sit amet interdum pretium.</p></div>
  <div class="grid-item" style="left:193px;top:60px"><div class="sq bg-blue"></div><p><span class="tiny-head">Title Goes Here</span>Phasellus eget commodo arcu. Nunc vitae semper dui. Integer venenatis, tellus sit amet interdum pretium.</p></div>
  <div class="grid-item" style="left:33px;top:100px"><div class="sq bg-teal"></div><p><span class="tiny-head">Title Goes Here</span>Phasellus eget commodo arcu. Nunc vitae semper dui. Integer venenatis, tellus sit amet interdum pretium.</p></div>
  <div class="grid-item" style="left:193px;top:100px"><div class="sq bg-cyan"></div><p><span class="tiny-head">Title Goes Here</span>Phasellus eget commodo arcu. Nunc vitae semper dui. Integer venenatis, tellus sit amet interdum pretium.</p></div>
  <div class="grid-item" style="left:33px;top:140px"><div class="sq bg-blue"></div><p><span class="tiny-head">Title Goes Here</span>Phasellus eget commodo arcu. Nunc vitae semper dui. Integer venenatis, tellus sit amet interdum pretium.</p></div>
  <div class="grid-item" style="left:193px;top:140px"><div class="sq bg-teal"></div><p><span class="tiny-head">Title Goes Here</span>Phasellus eget commodo arcu. Nunc vitae semper dui. Integer venenatis, tellus sit amet interdum pretium.</p></div>
  <div class="foot-brand brand">KESTRELMIND</div>
  <div class="foot-copy">KestrelMind © 2022 All Rights Reserved.<b>14</b></div>
</article>

<article class="slide" style="left:800px;top:1633px">
  <div class="dark" style="position:absolute;left:0;top:0;width:374px;height:95px"></div>
  <div class="h center white" style="top:16px">Heading Goes Here</div>
  <div class="tcard" style="left:39px"><div class="pic photo" role="img" aria-label="Handshake between a human and a robot hand" style="background:linear-gradient(135deg,#2f4a60,#14222f)"></div><div class="body bg-cyan"><b>Elit Vivamus Eu Dui Ex</b><p>Phasellus eget commodo arcu. Nunc vitae semper dui. Integer venenatis.</p></div><div class="circ bg-cyan"></div></div>
  <div class="tcard" style="left:143px"><div class="pic photo" role="img" aria-label="Hand on a digital network screen" style="background:linear-gradient(135deg,#3c63b8,#142458)"></div><div class="body bg-blue"><b>Gravida Sit Amet Risus</b><p>Phasellus eget commodo arcu. Nunc vitae semper dui. Integer venenatis.</p></div><div class="circ bg-blue"></div></div>
  <div class="tcard" style="left:247px"><div class="pic photo light" role="img" aria-label="Hands together with a digital overlay"></div><div class="body bg-teal"><b>Nulla Facilisi In Et</b><p>Phasellus eget commodo arcu. Nunc vitae semper dui. Integer venenatis.</p></div><div class="circ bg-teal"></div></div>
  <div class="foot-brand brand">KESTRELMIND</div>
  <div class="foot-copy">KestrelMind © 2022 All Rights Reserved.<b>15</b></div>
</article>

<!-- Row 6 -->
<article class="slide dark" style="left:26px;top:1856px">
  <div class="headart" role="img" aria-label="Bright cyan digital human head profile" style="left:190px;top:25px;width:170px;height:170px;background:radial-gradient(ellipse at 55% 50%,rgba(0,169,221,.8),rgba(0,148,212,.2) 55%,rgba(0,0,0,0) 72%)"></div>
  <div class="title" style="left:27px;top:70px"><span class="up">Section Break</span><br>Title Goes Here</div>
  <div class="desc" style="left:27px;top:120px">Lorem ipsum dolor sit amet, consectetur adipiscing elit.<br>dui ex. Curabitur dapibus dignissim dui, in molestie metus feugiat sed.</div>
</article>

<article class="slide" style="left:413px;top:1856px">
  <div class="dark" style="position:absolute;left:240px;top:0;width:134px;height:170px"></div>
  <div class="h" style="left:33px;top:30px">Heading Goes Here</div>
  <div class="small" style="left:33px;top:52px;width:135px">Nunc placerat, arcu nec mattis fermentum, nisl mauris convallis nunc, ut luctus nunc nisl id ex. Nam semper tristique mauris, et vestibulum leo fringilla vel.<br><br>Nunc vitae semper dui. Integer venenatis, tellus sit amet interdum pretium, erat neque rhoncus turpis, a aliquam augue ligula eget erat. Nunc placerat, arcu nec mattis fermentum, nisl mauris convallis nunc.<br><br>Nunc vitae semper dui. Integer venenatis, tellus sit amet interdum pretium, erat neque rhoncus turpis, a aliquam augue ligula eget erat. Nam semper tristique mauris.</div>
  <div class="num bg-cyan" style="top:30px"><span>1</span><p>Phasellus eget commodo arcu. Nunc vitae semper dui. Integer venenatis, tellus sit amet interdum pretium, erat neque rhoncus turpis.</p></div>
  <div class="num bg-blue" style="top:74px"><span>2</span><p>Phasellus eget commodo arcu. Nunc vitae semper dui. Integer venenatis, tellus sit amet interdum pretium, erat neque rhoncus turpis.</p></div>
  <div class="num bg-teal" style="top:118px"><span>3</span><p>Phasellus eget commodo arcu. Nunc vitae semper dui. Integer venenatis, tellus sit amet interdum pretium, erat neque rhoncus turpis.</p></div>
  <div class="foot-brand brand">KESTRELMIND</div>
  <div class="foot-copy">KestrelMind © 2022 All Rights Reserved.<b>17</b></div>
</article>

<article class="slide" style="left:800px;top:1856px">
  <svg width="374" height="210" style="position:absolute;left:0;top:0">
    <g fill="none" stroke-width="34">
      <circle cx="187" cy="172" r="89" pathLength="16" stroke="#1b2454" stroke-dasharray=".97 15.03" transform="rotate(180 187 172)"/>
      <circle cx="187" cy="172" r="89" pathLength="16" stroke="#0094D4" stroke-dasharray=".97 15.03" transform="rotate(202.5 187 172)"/>
      <circle cx="187" cy="172" r="89" pathLength="16" stroke="#0054AA" stroke-dasharray=".97 15.03" transform="rotate(225 187 172)"/>
      <circle cx="187" cy="172" r="89" pathLength="16" stroke="#00AB8E" stroke-dasharray=".97 15.03" transform="rotate(247.5 187 172)"/>
      <circle cx="187" cy="172" r="89" pathLength="16" stroke="#1b2454" stroke-dasharray=".97 15.03" transform="rotate(270 187 172)"/>
      <circle cx="187" cy="172" r="89" pathLength="16" stroke="#0094D4" stroke-dasharray=".97 15.03" transform="rotate(292.5 187 172)"/>
      <circle cx="187" cy="172" r="89" pathLength="16" stroke="#0054AA" stroke-dasharray=".97 15.03" transform="rotate(315 187 172)"/>
      <circle cx="187" cy="172" r="89" pathLength="16" stroke="#00AB8E" stroke-dasharray=".97 15.03" transform="rotate(337.5 187 172)"/>
    </g>
    <g fill="#fff">
      <circle cx="105" cy="155" r="3"/><circle cx="124" cy="110" r="3"/><circle cx="159" cy="80" r="3"/><circle cx="204" cy="77" r="3"/><circle cx="244" cy="98" r="3"/><circle cx="268" cy="133" r="3"/><circle cx="275" cy="165" r="3"/>
    </g>
  </svg>
  <div class="h center" style="top:126px;font-size:12px">Heading</div>
  <div class="small" style="left:140px;top:144px;width:94px;text-align:center">Phasellus eget commodo arcu. Nunc vitae semper dui. Integer venenatis, tellus sit amet interdum pretium.</div>
  <div class="ring-note" style="left:15px;top:135px">Phasellus eget commodo arcu. Nunc vitae semper dui.</div>
  <div class="ring-note" style="left:26px;top:88px">Phasellus eget commodo arcu. Nunc vitae semper dui.</div>
  <div class="ring-note" style="left:62px;top:45px">Phasellus eget commodo arcu. Nunc vitae semper dui.</div>
  <div class="ring-note" style="left:118px;top:20px">Phasellus eget commodo arcu. Nunc vitae semper dui.</div>
  <div class="ring-note" style="left:212px;top:20px">Phasellus eget commodo arcu. Nunc vitae semper dui.</div>
  <div class="ring-note" style="left:268px;top:45px">Phasellus eget commodo arcu. Nunc vitae semper dui.</div>
  <div class="ring-note" style="left:304px;top:88px">Phasellus eget commodo arcu. Nunc vitae semper dui.</div>
  <div class="ring-note" style="left:315px;top:135px">Phasellus eget commodo arcu. Nunc vitae semper dui.</div>
  <div class="foot-brand brand">KESTRELMIND</div>
  <div class="foot-copy">KestrelMind © 2022 All Rights Reserved.<b>18</b></div>
</article>

<!-- Row 7 -->
<article class="slide" style="left:219px;top:2079px">
  <div class="h center" style="top:16px">Heading Goes Here</div>
  <div class="rule" style="left:172px;top:36px;width:30px"></div>
  <svg width="374" height="210" style="position:absolute;left:0;top:0">
    <g fill="none" stroke-width="7">
      <circle cx="83" cy="92" r="34" stroke="#e3e6ea"/>
      <circle cx="83" cy="92" r="34" stroke="#00A9DD" pathLength="100" stroke-dasharray="35 65" transform="rotate(-90 83 92)"/>
      <circle cx="187" cy="92" r="34" stroke="#e3e6ea"/>
      <circle cx="187" cy="92" r="34" stroke="#0054AA" pathLength="100" stroke-dasharray="65 35" transform="rotate(-90 187 92)"/>
      <circle cx="291" cy="92" r="34" stroke="#e3e6ea"/>
      <circle cx="291" cy="92" r="34" stroke="#00AB8E" pathLength="100" stroke-dasharray="85 15" transform="rotate(-90 291 92)"/>
    </g>
    <g font-family="Ubuntu, sans-serif" font-size="13" text-anchor="middle">
      <text x="83" y="97" fill="#00A9DD">35%</text>
      <text x="187" y="97" fill="#0054AA">65%</text>
      <text x="291" y="97" fill="#00AB8E">85%</text>
    </g>
  </svg>
  <div class="donut-cap" style="left:43px"><b>Heading Goes Here</b><p>Rhoncus turpis, a aliquam augue ligula eget erat. Nunc placerat, arcu nec mattis fermentum, nisl mauris convallis nunc.</p></div>
  <div class="donut-cap" style="left:147px"><b>Heading Goes Here</b><p>Rhoncus turpis, a aliquam augue ligula eget erat. Nunc placerat, arcu nec mattis fermentum, nisl mauris convallis nunc.</p></div>
  <div class="donut-cap" style="left:251px"><b>Heading Goes Here</b><p>Rhoncus turpis, a aliquam augue ligula eget erat. Nunc placerat, arcu nec mattis fermentum, nisl mauris convallis nunc.</p></div>
  <div class="foot-brand brand">KESTRELMIND</div>
  <div class="foot-copy">KestrelMind © 2022 All Rights Reserved.<b>19</b></div>
</article>

<article class="slide dark" style="left:606px;top:2079px">
  <div class="photo" role="img" aria-label="Hands joined together in teamwork, tinted blue" style="left:150px;top:0;width:224px;height:200px;background:linear-gradient(120deg,rgba(40,70,140,0),rgba(120,150,200,.35))"></div>
  <div class="s-brand brand" style="left:26px;top:70px">KESTRELMIND <span class="dot"></span></div>
  <div class="contact">
    <h4>Contact Us</h4>
    <p>Lorem ipsum dolor sit amet, consectetur adipiscing</p>
    <ul>
      <li><svg width="5" height="5"><path d="M1 0.5 L2 0.5 L2.5 1.8 L1.8 2.3 Q2.4 3.4 3.2 3.6 L3.7 3 L4.8 3.5 L4.6 4.6 Q1 4.6 0.5 1 Z" fill="#00A9DD"/></svg>345-555-0142</li>
      <li><i></i>hello@kestrelmind.com</li>
      <li><svg width="5" height="5"><circle cx="2.5" cy="2.5" r="2" fill="none" stroke="#00A9DD" stroke-width=".6"/><line x1=".5" y1="2.5" x2="4.5" y2="2.5" stroke="#00A9DD" stroke-width=".5"/></svg>www.kestrelmind.com</li>
    </ul>
  </div>
  <div class="strip">KestrelMind © 2022 All Rights Reserved.</div>
</article>

</body>
</html>
```